NEW Modern Sleek Business Card for VR Language Startup

Our startup is using VR to lead the next wave of world language education. We need a two-sided business card that introduces the larger organization (Quorvel Language Inc) and our contact info on one side and shows the product, Lumidrasca, on the other side.

Side 1 (contact info)= Quorvel Logo and Contact info (name, title, phone, email)

Side 2 (product)= Lumidrasc logo, text, and website
Text= Culturally Immersive Language Learning Games
Website= www.lumidrasc.example

Target Market(s)

Education, Technology

Contact Information for Business Card

Contact info will be updated upon approval of the design. For now, put this as a placeholder.

Perry Hollins
Founder & CEO
phollins@mailtrove.example
(555)-014-2736

Font styles to use
Other font styles liked:
• Gibson and Century Gothic are the brand fonts

Requirements
Nice to have
• I would love to see cohesion between the design and colors of the two logos. I have attached a few business card designs that I like, so you can get a feel for my preferred style.

```html
<!DOCTYPE html>
<html lang="en">
<head>
<meta charset="utf-8">
<title>Lumidrasc &amp; Quorvel Language – Business Card</title>
<link href="https://fonts.googleapis.com/css2?family=Montserrat:wght@500;600;700&family=Questrial&family=Josefin+Sans:wght@300;600&display=swap" rel="stylesheet">
<style>
  :root {
    --page: #ffffff;
    --navy-deep: #1d1f5e;
    --navy: #23307f;
    --royal: #2a3c9c;
    --circuit-a: #2350a8;
    --circuit-b: #1f3488;
    --strip-a: #1c64c4;
    --strip-b: #2a8ee0;
    --accent: #f0584f;
    --white: #ffffff;
  }
  * { box-sizing: border-box; margin: 0; padding: 0; }
  html, body { width: 1200px; height: 1000px; overflow: hidden; background: var(--page); }
  .canvas { position: relative; width: 1200px; height: 1000px; }

  .card {
    position: absolute;
    left: 296px;
    width: 607px;
    height: 347px;
    overflow: hidden;
    color: var(--white);
  }
  .card--product { top: 110px; background: var(--navy); }
  .card--contact { top: 543px; background: linear-gradient(160deg, var(--royal) 0%, var(--navy) 55%, var(--navy-deep) 100%); }

  /* product side */
  .pattern-panel {
    position: absolute;
    top: 0;
    height: 100%;
  }
  .pattern-panel--left { left: 0; width: 176px; background: linear-gradient(150deg, var(--circuit-a), var(--circuit-b)); }
  .pattern-panel--right { right: 0; width: 191px; background: linear-gradient(210deg, var(--circuit-a), var(--circuit-b)); }
  .product-center {
    position: absolute;
    left: 176px;
    width: 240px;
    top: 0;
    height: 100%;
    background: radial-gradient(circle at 50% 20%, #2b3a9a 0%, var(--navy) 70%);
  }
  .product-brand {
    position: absolute;
    left: 0; right: 0;
    top: 80px;
    text-align: center;
  }
  .brand-dot {
    display: block;
    width: 54px; height: 54px;
    margin: 0 auto 24px;
    border-radius: 50%;
    background: var(--white);
  }
  .product-name {
    font-family: "Montserrat", sans-serif;
    font-weight: 700;
    font-size: 23px;
    letter-spacing: 0.2px;
  }
  .product-tagline {
    position: absolute;
    left: 0; right: 0;
    top: 224px;
    text-align: center;
    font-family: "Questrial", sans-serif;
    font-size: 9.6px;
    white-space: nowrap;
  }
  .product-url {
    position: absolute;
    left: 0; right: 0;
    top: 304px;
    text-align: center;
    font-family: "Montserrat", sans-serif;
    font-weight: 600;
    font-size: 16.5px;
    letter-spacing: 0.4px;
  }

  /* contact side */
  .brand-panel {
    position: absolute;
    left: 0; top: 0;
    width: 290px; height: 100%;
    background: linear-gradient(150deg, #2553ad 0%, var(--circuit-b) 60%, #1f2f7e 100%);
  }
  .brand-panel::after {
    content: "";
    position: absolute;
    right: 0; top: 0;
    width: 2px; height: 100%;
    background: #2d5fc0;
  }
  .company-brand {
    position: absolute;
    left: 0; width: 290px;
    top: 92px;
    text-align: center;
  }
  .company-brand .brand-dot {
    width: 76px; height: 76px;
    margin-bottom: 32px;
    background: var(--accent);
  }
  .company-name {
    font-family: "Montserrat", sans-serif;
    font-weight: 600;
    font-size: 27px;
    letter-spacing: 5px;
    line-height: 1.35;
    text-transform: uppercase;
  }
  .person {
    position: absolute;
    right: 48px;
    top: 50px;
    text-align: right;
  }
  .person-name {
    font-family: "Josefin Sans", sans-serif;
    font-size: 28px;
    letter-spacing: 2px;
    line-height: 1;
    text-transform: uppercase;
  }
  .person-name strong { font-weight: 600; }
  .person-name span { font-weight: 300; }
  .person-title {
    margin-top: 4px;
    font-family: "Montserrat", sans-serif;
    font-weight: 700;
    font-size: 11px;
    letter-spacing: 2.4px;
  }
  .icon-strip {
    position: absolute;
    left: 290px;
    top: 156px;
    width: 48px;
    height: 135px;
    background: linear-gradient(90deg, var(--strip-a), var(--strip-b));
  }
  .contact-list { list-style: none; }
  .contact-item {
    position: absolute;
    left: 305px;
    display: flex;
    align-items: center;
    font-family: "Montserrat", sans-serif;
    font-weight: 600;
    font-size: 12.5px;
    letter-spacing: 1.1px;
    white-space: nowrap;
  }
  .contact-item svg { width: 18px; height: 18px; flex: none; margin-right: 26px; }
  .contact-item--address { top: 186px; }
  .contact-item--phone { top: 215px; }
  .contact-item--email { top: 244px; }
</style>
</head>
<body>
<main class="canvas">

  <section class="card card--product" aria-label="Product side">
    <div class="pattern-panel pattern-panel--left" role="img" aria-label="Blue circuit board line pattern"></div>
    <div class="product-center"></div>
    <div class="pattern-panel pattern-panel--right" role="img" aria-label="Blue circuit board line pattern"></div>

    <div class="product-brand">
      <span class="brand-dot"></span>
      <h1 class="product-name">Lumidrasc</h1>
    </div>
    <p class="product-tagline">Culturally Immersive Language Learning Games</p>
    <p class="product-url">www.lumidrasc.example</p>
  </section>

  <section class="card card--contact" aria-label="Contact side">
    <div class="brand-panel" role="img" aria-label="Blue circuit board line pattern"></div>
    <div class="company-brand">
      <span class="brand-dot"></span>
      <h2 class="company-name">Quorvel<br>Language</h2>
    </div>

    <div class="person">
      <p class="person-name"><strong>Perry</strong> <span>Hollins</span></p>
      <p class="person-title">Founder &amp; CEO</p>
    </div>

    <div class="icon-strip"></div>
    <ul class="contact-list">
      <li class="contact-item contact-item--address">
        <svg viewBox="0 0 24 24" aria-hidden="true"><path d="M12 2a7 7 0 0 0-7 7c0 5 7 13 7 13s7-8 7-13a7 7 0 0 0-7-7zm0 9.5A2.5 2.5 0 1 1 12 6.5a2.5 2.5 0 0 1 0 5z" fill="#fff"/></svg>
        123 Dummy, Lorem Ipsum
      </li>
      <li class="contact-item contact-item--phone">
        <svg viewBox="0 0 24 24" aria-hidden="true"><path d="M6.6 10.8a15 15 0 0 0 6.6 6.6l2.2-2.2c.3-.3.7-.4 1-.2 1.1.4 2.3.6 3.6.6.6 0 1 .4 1 1V20c0 .6-.4 1-1 1A17 17 0 0 1 3 4c0-.6.4-1 1-1h3.5c.6 0 1 .4 1 1 0 1.3.2 2.5.6 3.6.1.3 0 .7-.2 1z" fill="#fff"/></svg>
        (555)-014-2736
      </li>
      <li class="contact-item contact-item--email">
        <svg viewBox="0 0 24 24" aria-hidden="true"><rect x="3" y="6" width="18" height="12" fill="#fff"/><path d="M3 6l9 7 9-7M3 18l7-6M21 18l-7-6" stroke="#2350a8" stroke-width="1.4" fill="none"/></svg>
        phollins@mailtrove.example
      </li>
    </ul>
  </section>

</main>
</body>
</html>
```